Freelance business trainer needs a new business card

My business is called Tbrite. I provide training in the workplace on management, coaching and mentoring, and customer service topics for a variety of businesses, colleges and private training providers, and teach on management programs. I need a professional but eye catching business card. Business colours grey and orange. My name Linda Marchbank; Tel 07853 416207; email lmarchbank@tbrite.co.uk; website www.tbrite.co.uk.
Happy to have some sort of logo on front and details on back or all on one side
Target Market(s)
SME businesses and colleges - workshops i run are for adults in the workplace
Industry/Entity Type
Training
Look and feel

```html
<!DOCTYPE html>
<html lang="en">
<head>
<meta charset="utf-8">
<title>Tbrite – Business Card</title>
<link rel="stylesheet" href="https://fonts.googleapis.com/css2?family=Montserrat:wght@300;400;700;800&display=swap">
<style>
  :root {
    --grey: #525355;
    --grey-dark: #47484a;
    --orange: #f39a1e;
    --white: #ffffff;
    --backdrop: #e9e6e2;
  }
  * { box-sizing: border-box; margin: 0; padding: 0; }
  html, body {
    width: 1200px; height: 1000px; overflow: hidden;
    background: var(--backdrop);
    font-family: "Montserrat", Arial, sans-serif;
  }
  .sheet {
    width: 1200px; height: 1000px;
    display: flex; flex-direction: column; align-items: center; justify-content: center;
    gap: 40px;
  }
  .card {
    position: relative;
    width: 760px; height: 434px;
    overflow: hidden;
    box-shadow: 0 6px 18px rgba(0,0,0,0.18);
  }

  /* Front */
  .card--front { background: var(--white); }
  .front-brand {
    position: absolute; left: 0; right: 0; top: 120px;
    display: flex; align-items: center; justify-content: center; gap: 18px;
  }
  .brand-dot {
    width: 56px; height: 56px; border-radius: 50%;
    background: var(--orange);
  }
  .front-brand__name {
    font-weight: 800; font-size: 78px; letter-spacing: -1px;
    color: var(--grey);
  }
  .front-band {
    position: absolute; left: 0; right: 0; bottom: 0; height: 62px;
    background: var(--grey);
    display: flex; align-items: center; justify-content: center;
  }
  .front-band__web {
    color: var(--white); font-size: 15px; font-weight: 400; letter-spacing: 0.5px;
  }

  /* Back */
  .card--back { background: var(--grey); }
  .back-name {
    position: absolute; right: 48px; top: 44px;
    font-weight: 800; font-size: 60px; letter-spacing: -1px;
    color: var(--white);
  }
  .back-dot {
    position: absolute; left: 60px; top: 140px;
    width: 110px; height: 110px; border-radius: 50%;
    background: var(--orange);
  }
  .person {
    position: absolute; right: 372px; bottom: 58px;
    text-align: right; white-space: nowrap;
  }
  .person__name {
    color: var(--orange); font-weight: 700; font-size: 26px; line-height: 1.2;
  }
  .person__role {
    color: var(--white); font-weight: 300; font-size: 30px; line-height: 1.2;
  }
  .divider {
    position: absolute; left: 404px; top: 236px; width: 2px; height: 96px;
    background: rgba(255,255,255,0.55);
  }
  .contacts {
    position: absolute; left: 422px; top: 240px;
    list-style: none; display: flex; flex-direction: column; gap: 22px;
  }
  .contact {
    display: flex; align-items: center; gap: 10px; white-space: nowrap;
    color: var(--white); font-weight: 300; font-size: 19px;
  }
  .contact__icon { width: 28px; height: 28px; flex: none; }
</style>
</head>
<body>
<main class="sheet">

  <section class="card card--front" aria-label="Card front">
    <div class="front-brand">
      <span class="brand-dot"></span>
      <span class="front-brand__name">Tbrite</span>
    </div>
    <div class="front-band">
      <span class="front-band__web">www.tbrite.co.uk</span>
    </div>
  </section>

  <section class="card card--back" aria-label="Card back">
    <div class="back-name">Tbrite</div>
    <span class="back-dot"></span>

    <div class="person">
      <p class="person__name">Linda Marchbank</p>
      <p class="person__role">Business trainer</p>
    </div>

    <span class="divider"></span>

    <ul class="contacts">
      <li class="contact">
        <svg class="contact__icon" viewBox="0 0 30 30" aria-hidden="true">
          <circle cx="15" cy="15" r="14" fill="#f39a1e"/>
          <circle cx="15" cy="15" r="11" fill="none" stroke="#525355" stroke-width="1.2"/>
          <rect x="11" y="7.5" width="8" height="15" rx="1.5" fill="none" stroke="#525355" stroke-width="1.6"/>
          <rect x="12.5" y="9.5" width="5" height="4" fill="#525355"/>
          <circle cx="15" cy="19.5" r="1" fill="#525355"/>
        </svg>
        <span>07853 416207</span>
      </li>
      <li class="contact">
        <svg class="contact__icon" viewBox="0 0 30 30" aria-hidden="true">
          <circle cx="15" cy="15" r="14" fill="#f39a1e"/>
          <circle cx="15" cy="15" r="11" fill="none" stroke="#525355" stroke-width="1.2"/>
          <rect x="8" y="10" width="14" height="10" fill="none" stroke="#525355" stroke-width="1.6"/>
          <path d="M8 10 L15 16 L22 10" fill="none" stroke="#525355" stroke-width="1.6"/>
        </svg>
        <span>lmarchbank@tbrite.co.uk</span>
      </li>
    </ul>
  </section>

</main>
</body>
</html>
```